Company or website name
- zestoplex
- Links to the website
- www.zestoplex.com
- Describe your company and organization and target audience
- I need a website design for a new kids vitamins brand called ZESTOPLEX.   This brand is built on the foundations that it has everything you need, nothing that you dont (e.g. GMO, Animal Content, Soy, Dairy, Gelatin) and is right for everyone. This is a brand that appeals to millenial moms who want only the best for their kids.  It's colorful, bold, vibrant yet credible because all formulas are clinically tested.
- Other Facts

```html
<!DOCTYPE html>
<html lang="en">
<head>
<meta charset="utf-8">
<title>Zestoplex – Kids Vitamins</title>
<link href="https://fonts.googleapis.com/css2?family=Montserrat:wght@400;500;600;700;800&display=swap" rel="stylesheet">
<style>
:root{
  --magenta:#c1408f;
  --purple:#a55aa8;
  --deep-purple:#8a4fa6;
  --pink:#e8699a;
  --orange:#f6b052;
  --coral:#ef6a55;
  --red:#e9483b;
  --cyan:#7fd0e6;
  --yellow:#f8e36a;
  --white:#ffffff;
  --ink:#3a2a4a;
}
*{box-sizing:border-box;margin:0;padding:0}
html,body{width:674px;height:1200px;overflow:hidden;background:var(--white)}
body{font-family:"Montserrat",Arial,sans-serif;color:var(--ink)}
.canvas{position:relative;width:674px;height:1200px;overflow:hidden;background:var(--white)}
.abs{position:absolute}
.bubble{position:absolute;border-radius:50%;opacity:.35}

/* header */
.hero-shape{left:0;top:0}
.logo{left:66px;top:46px;font-size:19px;font-weight:800;letter-spacing:.5px;color:var(--magenta)}
.nav{right:0;top:26px;width:360px;height:24px;font-size:10px;font-weight:500;color:var(--white)}
.nav a{color:var(--white);text-decoration:none;position:absolute;top:6px;white-space:nowrap}
.nav .active{border:1px solid var(--white);border-radius:12px;padding:5px 11px;top:0}
.hero-art{left:395px;top:58px;width:240px;height:200px;border-radius:50% 45% 40% 50%;
  background:radial-gradient(circle at 45% 40%,#e3a05a 0 30%,#d8876a 45%,rgba(233,120,140,0) 72%)}
.headline{left:64px;top:116px;font-size:38px;line-height:43px;font-weight:700;color:var(--magenta);white-space:nowrap}
.hero-copy{left:65px;top:216px;width:225px;font-size:6.5px;line-height:9px;color:var(--magenta)}

/* intro banner */
.intro{left:8px;top:287px;width:659px;height:192px;border-radius:28px;
  background:linear-gradient(90deg,var(--orange) 0%,#ee8a80 35%,var(--pink) 60%,var(--purple) 100%)}
.dots{left:310px;top:27px;display:flex;gap:16px}
.dots span{width:6px;height:6px;border-radius:50%;border:1px solid var(--white)}
.dots span:first-child{background:var(--white)}
.intro-title{left:58px;top:44px;font-size:25px;line-height:30px;font-weight:600;color:var(--white);white-space:nowrap}
.intro-copy{left:262px;top:52px;width:152px;font-size:6.3px;line-height:9.2px;color:var(--white)}
.intro-copy p+p{margin-top:5px}
.intro-tagline{right:55px;top:40px;text-align:right;font-size:25px;line-height:26px;font-weight:600;color:var(--white);white-space:nowrap}
.pill{position:absolute;border:1px solid var(--white);border-radius:12px;width:70px;height:22px;
  font-size:8.5px;font-weight:500;color:var(--white);display:flex;align-items:center;justify-content:center}

/* products */
.section-title{left:0;width:674px;top:500px;text-align:center;font-size:30px;font-weight:700;color:var(--magenta)}
.section-copy{left:135px;top:538px;width:404px;text-align:center;font-size:6.3px;line-height:9.2px;color:var(--magenta)}
.product-range{left:84px;top:590px;width:516px;height:208px;border-radius:24px 24px 18px 18px;
  background:linear-gradient(90deg,#5cc3d8 0%,#8a5cc0 18%,#c860b8 33%,#ef5a5a 50%,#f08a3a 66%,#f3b53a 82%,#3fbf9a 100%);opacity:.85}

/* featured */
.feature-card{left:0;top:804px;width:217px;height:130px;border-radius:0 26px 26px 0;
  background:linear-gradient(135deg,var(--coral) 0%,#e8687a 55%,var(--purple) 100%)}
.feature-flavour{left:65px;top:22px;font-size:7px;color:var(--white)}
.feature-name{left:65px;top:38px;font-size:21px;line-height:24px;font-weight:600;color:var(--white);white-space:nowrap}
.feature-copy{left:65px;top:92px;width:130px;font-size:6.5px;line-height:9px;color:var(--white)}
.flavour-label{left:276px;top:820px;font-size:19px;font-weight:700;color:var(--red);letter-spacing:.3px}
.buy-btn{left:302px;top:863px;width:86px;height:34px;border-radius:9px;background:var(--red);
  color:var(--white);font-size:12px;font-weight:500;display:flex;align-items:center;justify-content:center}

/* badges */
.badges{left:152px;top:956px;display:flex;gap:11.5px}
.badge{width:47px;height:47px;border-radius:50%;border:3px solid var(--white);box-shadow:0 0 0 1.5px var(--c);background:var(--c)}

/* footer */
.footer-wave{left:0;top:1015px}
.contact{left:64px;width:220px;height:40px;color:var(--white)}
.contact .main{position:absolute;left:30px;top:-3px;font-size:12.5px;font-weight:500;white-space:nowrap}
.contact .sub{position:absolute;left:30px;top:15px;font-size:5.8px;line-height:8px;white-space:nowrap}
.divider{width:1px;height:78px;background:rgba(255,255,255,.6);top:1100px}
.social{left:327px;top:1127px;display:flex;gap:8px}
.social span{width:11px;height:11px;border-radius:2px;background:var(--white)}
.social-copy{left:318px;top:1152px;width:100px;text-align:center;font-size:4.6px;line-height:6px;color:var(--white)}
.brand-foot{left:464px;top:1116px;font-size:16px;font-weight:800;color:var(--white);letter-spacing:.3px}
.brand-mark{left:590px;top:1114px;width:20px;height:20px;border-radius:50%;background:#e9a85a}
.brand-url{left:477px;top:1136px;font-size:9.5px;font-weight:500;color:var(--white)}
</style>
</head>
<body>
<div class="canvas">

  <span class="bubble" style="left:-8px;top:205px;width:30px;height:30px;background:#f3a3c5"></span>
  <span class="bubble" style="left:60px;top:245px;width:50px;height:50px;background:#f8e36a"></span>
  <span class="bubble" style="left:0;top:265px;width:26px;height:26px;background:#c7a7e0"></span>
  <span class="bubble" style="left:330px;top:222px;width:22px;height:22px;background:#f6c08a"></span>
  <span class="bubble" style="left:274px;top:256px;width:20px;height:20px;background:#f3a3c5"></span>
  <span class="bubble" style="left:26px;top:492px;width:52px;height:52px;background:#f6c08a"></span>
  <span class="bubble" style="left:0;top:560px;width:26px;height:26px;background:#b7a6e6"></span>
  <span class="bubble" style="left:558px;top:470px;width:42px;height:42px;background:#f3a3c5"></span>
  <span class="bubble" style="left:647px;top:525px;width:34px;height:34px;background:#f3a3c5"></span>
  <span class="bubble" style="left:596px;top:544px;width:26px;height:26px;background:#9fd7b4"></span>
  <span class="bubble" style="left:640px;top:702px;width:44px;height:44px;background:#f6c08a"></span>
  <span class="bubble" style="left:596px;top:762px;width:28px;height:28px;background:#b7a6e6"></span>
  <span class="bubble" style="left:0;top:768px;width:22px;height:22px;background:#f8e36a"></span>
  <span class="bubble" style="left:522px;top:818px;width:34px;height:34px;background:#f6c08a"></span>
  <span class="bubble" style="left:612px;top:860px;width:34px;height:34px;background:#f3a3c5"></span>
  <span class="bubble" style="left:28px;top:952px;width:38px;height:38px;background:#7fd0e6"></span>
  <span class="bubble" style="left:649px;top:1018px;width:30px;height:30px;background:#f6c08a"></span>

  <svg class="abs hero-shape" width="674" height="290" viewBox="0 0 674 290" aria-hidden="true">
    <defs>
      <linearGradient id="heroGrad" x1="0" y1="0" x2="1" y2="1">
        <stop offset="0" stop-color="#e8699a"/>
        <stop offset=".6" stop-color="#c064a8"/>
        <stop offset="1" stop-color="#9b5aa6"/>
      </linearGradient>
    </defs>
    <path d="M210 0 H674 V250 C630 240 590 180 520 200 C470 215 420 180 380 120 C340 60 280 20 210 0 Z" fill="url(#heroGrad)"/>
    <path d="M330 80 C360 50 430 60 470 70 C520 80 560 60 600 90 C640 120 610 170 560 180 C500 190 430 170 390 150 C340 125 310 105 330 80 Z" fill="#7fd0e6" opacity=".85"/>
    <path d="M400 170 C420 140 480 150 520 170 C560 190 560 240 520 268 C480 290 420 275 405 240 C395 215 390 190 400 170 Z" fill="#f8e36a"/>
    <path d="M590 90 C620 70 660 80 674 95 V160 C650 150 600 130 590 90 Z" fill="#f6c08a" opacity=".8"/>
  </svg>

  <div class="abs logo">ZESTOPLEX</div>
  <nav class="abs nav">
    <a href="#" style="left:30px">Home</a>
    <a href="#" style="left:88px">Contact</a>
    <a href="#" class="active" style="left:146px">About</a>
    <a href="#" style="left:218px">Product</a>
    <a href="#" style="left:278px">&#9654; Login</a>
  </nav>

  <div class="abs hero-art" role="img" aria-label="Illustration of a cartoon teddy bear holding two vitamin gummy bottles"></div>

  <h1 class="abs headline">Making Kids<br>Healty &amp; Smart</h1>
  <p class="abs hero-copy">Lorem ipsum dolor sit amet, consectetuer adipiscing elit, sed diam nonum. Lorem ipsum dolor sit amet, consectetuer adipiscing elit, sed diam nonum</p>

  <section class="abs intro">
    <div class="abs dots"><span></span><span></span><span></span></div>
    <h2 class="abs intro-title">What is<br>Zestoplex ?</h2>
    <div class="abs intro-copy">
      <p>Lorem ipsum dolor sit amet, consectetuer adipiscing elit, sed diam nonum. Lorem ipsum dolor sit amet, consectetuer adipiscing elit, sed diam nonum Lorem ipsum dolor sit amet, consectetuer adipiscing elit, sed diam nonum. Lorem ipsum dolor sit amet, consectetuer adipiscing elit, sed diam nonum</p>
      <p>dipiscing elit, sed diam nonum. Lorem ipsum dolor sit amet, consectetuer adipiscing elit, sed diam nonum</p>
    </div>
    <p class="abs intro-tagline">Healty Body<br>Smart<br>Healty Mind</p>
    <span class="pill" style="left:58px;top:159px">Read more</span>
    <span class="pill" style="left:533px;top:159px">Read more</span>
  </section>

  <h2 class="abs section-title">Our Product</h2>
  <p class="abs section-copy">Lorem ipsum dolor sit amet, consectetuer adipiscing elit, sed diam nonum. Lorem ipsum dolor sit amet, consectetuer adipiscing elit, sed diam nonum Lorem ipsum dolor sit amet, consectetuer adipiscing elit, sed diam nonum. Lorem ipsum dolor sit amet, consectetuer adipiscing elit, sed diam nonum Lorem ipsum dolor sit amet, consectetuer adipiscing elit, sed diam nonum. Lorem ipsum dolor sit amet, consectetuer adipiscing elit, sed diam nonum</p>
  <div class="abs product-range" role="img" aria-label="Row of seven colourful gummy vitamin bottles, the strawberry bottle in the centre"></div>

  <div class="abs feature-card">
    <p class="abs feature-flavour">Strawberry</p>
    <h3 class="abs feature-name">Ready to<br>achieve</h3>
    <p class="abs feature-copy">Support your brain's learning, concentration and reasoning</p>
  </div>
  <svg class="abs" style="left:205px;top:826px" width="66" height="10" viewBox="0 0 66 10" aria-hidden="true">
    <circle cx="3" cy="5" r="2.5" fill="#e9483b"/>
    <line x1="9" y1="5" x2="66" y2="5" stroke="#e9483b" stroke-width="1.5" stroke-dasharray="8 5"/>
  </svg>
  <p class="abs flavour-label">STRAWBERRY</p>
  <svg class="abs" style="left:264px;top:870px" width="28" height="20" viewBox="0 0 28 20" aria-hidden="true">
    <path d="M2 10 L12 2 V7 H26 V13 H12 V18 Z" fill="#b45fae"/>
  </svg>
  <div class="abs buy-btn">Buy now</div>
  <svg class="abs" style="left:398px;top:870px" width="28" height="20" viewBox="0 0 28 20" aria-hidden="true">
    <path d="M26 10 L16 2 V7 H2 V13 H16 V18 Z" fill="#ef8a4a"/>
  </svg>

  <div class="abs badges" aria-label="Product certifications">
    <span class="badge" style="--c:#3aa88a"></span>
    <span class="badge" style="--c:#f3b52b"></span>
    <span class="badge" style="--c:#1aa0a6"></span>
    <span class="badge" style="--c:#6c4fa0"></span>
    <span class="badge" style="--c:#b0459a"></span>
    <span class="badge" style="--c:#ef7a3a"></span>
    <span class="badge" style="--c:#e8494d"></span>
  </div>

  <svg class="abs footer-wave" width="674" height="185" viewBox="0 0 674 185" aria-hidden="true">
    <defs>
      <linearGradient id="footGrad" x1="0" y1="0" x2="1" y2="0">
        <stop offset="0" stop-color="#8a4fa6"/>
        <stop offset=".55" stop-color="#c35ea2"/>
        <stop offset="1" stop-color="#ec6b92"/>
      </linearGradient>
    </defs>
    <path d="M0 40 C120 0 240 50 360 35 C480 20 580 10 674 35 V185 H0 Z" fill="url(#footGrad)"/>
    <path d="M0 155 C90 135 170 150 250 185 H0 Z" fill="#7a5ab8" opacity=".55"/>
  </svg>

  <div class="abs contact" style="top:1078px">
    <svg class="abs" style="left:0;top:0" width="20" height="20" viewBox="0 0 20 20" aria-hidden="true">
      <circle cx="10" cy="10" r="9" fill="none" stroke="#fff" stroke-width="1.3"/>
      <path d="M7 5.5 L8.6 5.5 L9.3 8 L8.2 8.9 C8.8 10.3 9.7 11.2 11.1 11.8 L12 10.7 L14.5 11.4 L14.5 13 C14.5 13.6 14 14 13.4 14 C9.6 13.7 6.3 10.4 6 6.6 C6 6 6.4 5.5 7 5.5 Z" fill="#fff"/>
    </svg>
    <span class="main">+00 (1) 5550 1234</span>
    <span class="sub">Monday-Sunday<br>08.00 AM - 21.00 PM</span>
  </div>
  <div class="abs contact" style="top:1133px">
    <svg class="abs" style="left:0;top:0" width="20" height="20" viewBox="0 0 20 20" aria-hidden="true">
      <circle cx="10" cy="10" r="9" fill="none" stroke="#fff" stroke-width="1.3"/>
      <rect x="5.5" y="7" width="9" height="6.5" rx="1" fill="#fff"/>
      <path d="M5.8 7.4 L10 10.6 L14.2 7.4" fill="none" stroke="#a55aa8" stroke-width="1"/>
    </svg>
    <span class="main">noreply@zestoplex.com</span>
    <span class="sub">Monday-Sunday<br>24 HOURS</span>
  </div>

  <span class="abs divider" style="left:297px"></span>
  <span class="abs divider" style="left:438px"></span>

  <div class="abs social" aria-label="Social links"><span></span><span></span><span></span><span></span></div>
  <p class="abs social-copy">Lorem ipsum dolor sit amet, consectetuer adipiscing elit, sed diam nonum</p>

  <div class="abs brand-foot">ZESTOPLEX</div>
  <span class="abs brand-mark"></span>
  <div class="abs brand-url">www.zestoplex.com</div>

</div>
</body>
</html>
```